Boost Your Sales 100% In Prime Picks 2013 With The Velmora 300

Please vist www.brightmerrow.net, use all the images of the current advertisers there on the Home page and create a better flyer from this attached old flyer.

Industry/Entity Type

Sales

```html
<!DOCTYPE html>
<html lang="en">
<head>
<meta charset="utf-8">
<title>Prime Picks 2013 Flyer</title>
<link href="https://fonts.googleapis.com/css2?family=Roboto+Condensed:ital,wght@0,400;0,700;0,900;1,400;1,700;1,900&display=swap" rel="stylesheet">
<style>
:root{
  --frame:#d4d4d4;
  --ink:#0d0d0d;
  --white:#ffffff;
  --hot:#f24a1f;
  --red:#e21b23;
  --stripe-red:#e5261f;
  --stripe-orange:#f05a22;
  --stripe-amber:#f7941d;
  --stripe-yellow:#fdc10e;
  --blue:#1a5fc4;
  --navy:#1b3f8f;
}
*{margin:0;padding:0;box-sizing:border-box}
html,body{width:900px;height:1200px;overflow:hidden}
body{background:var(--frame);font-family:"Roboto Condensed",Arial,sans-serif;position:relative}
.flyer{position:absolute;left:24px;top:24px;width:852px;height:1152px;background:var(--ink);overflow:hidden;box-shadow:0 4px 14px rgba(0,0,0,.35)}
.photo-strip{position:absolute;left:0;width:100%}
.photo-strip--top{top:0;height:126px;background:linear-gradient(90deg,#7a5a3c,#2a5a9a 25%,#c9c2b5 45%,#1f5a3e 62%,#a8826a 82%,#5c6f85)}
.photo-strip--food{top:276px;height:36px;background:linear-gradient(90deg,#b8352a,#d9a441 40%,#6b8f3a 70%,#c2562c)}
.brand-tag{position:absolute;color:var(--white);font-weight:700;font-size:17px;letter-spacing:.5px}
.headline-band{position:absolute;top:126px;left:0;width:100%;height:150px;text-align:center;background:var(--ink)}
.headline-band .kicker{color:var(--white);font-weight:900;font-style:italic;font-size:44px;margin-top:14px;letter-spacing:.5px}
.headline-band .event{color:var(--hot);font-weight:900;font-style:italic;font-size:92px;line-height:88px;letter-spacing:1px}
.offer{position:absolute;top:312px;left:0;width:100%;height:588px;background:linear-gradient(90deg,var(--stripe-red) 0 86px,var(--stripe-orange) 86px 172px,var(--stripe-amber) 172px 258px,var(--stripe-yellow) 258px 100%)}
.discount-tag{position:absolute;right:18px;top:4px;width:300px;height:180px}
.pitch{position:absolute;left:0;width:100%;text-align:center;color:var(--red);font-weight:900;font-style:italic}
.pitch--lead{top:196px;font-size:72px;line-height:72px}
.pitch--big{top:266px;font-size:116px;line-height:112px}
.guarantee{position:absolute;top:382px;left:0;width:100%;text-align:center;font-weight:900;font-style:italic;font-size:38px;line-height:42px;color:var(--red)}
.guarantee .light{color:var(--white)}
.agent-box{position:absolute;left:258px;top:490px;width:360px;height:96px;background:var(--blue);border:3px solid var(--white);transform:rotate(-4deg);text-align:center;color:var(--white);font-style:italic;box-shadow:0 3px 8px rgba(0,0,0,.3)}
.agent-box .cta{font-weight:700;font-size:34px;line-height:40px;margin-top:6px}
.agent-box .phone{font-weight:900;font-size:42px;line-height:44px}
.photo-strip--bottom{top:900px;height:186px;background:linear-gradient(90deg,#5a6f8c 0 22%,#b23c4a 22% 44%,#d9c9b2 44% 64%,#3a4c6a 64% 100%)}
.footer{position:absolute;top:1086px;left:0;width:100%;height:66px;background:var(--ink);text-align:center;color:var(--white)}
.footer .rights{font-weight:700;font-style:italic;font-size:26px;margin-top:6px;letter-spacing:.5px}
.footer .sponsor{font-size:16px;letter-spacing:.3px}
</style>
</head>
<body>
<main class="flyer">
  <div class="photo-strip photo-strip--top" role="img" aria-label="Collage of advertiser storefronts, products and shoppers">
    <span class="brand-tag" style="left:10px;top:8px">Evermist Aroma</span>
    <span class="brand-tag" style="left:230px;top:8px;color:#1a5fc4">Valmore</span>
  </div>

  <header class="headline-band">
    <p class="kicker">JOIN THE VELMORA 300 NOW IN</p>
    <h1 class="event">PRIME PICKS 2013</h1>
  </header>

  <div class="photo-strip photo-strip--food" role="img" aria-label="Strip of featured food and product photos"></div>

  <section class="offer">
    <svg class="discount-tag" viewBox="0 0 300 180" aria-label="Globally linking all discounts to you">
      <path d="M14 40 C 40 10, 70 30, 60 70" fill="none" stroke="#1b3f8f" stroke-width="3"/>
      <g transform="rotate(-12 160 90)">
        <path d="M60 40 L270 40 L270 150 L60 150 L30 95 Z" fill="#fff" stroke="#1b3f8f" stroke-width="5"/>
        <circle cx="62" cy="95" r="8" fill="none" stroke="#1b3f8f" stroke-width="4"/>
        <text x="170" y="78" text-anchor="middle" font-family="Roboto Condensed, sans-serif" font-weight="900" font-style="italic" font-size="26" fill="#1a5fc4">GLOBALLY LINKING</text>
        <text x="170" y="112" text-anchor="middle" font-family="Roboto Condensed, sans-serif" font-weight="900" font-style="italic" font-size="26" fill="#1a5fc4">ALL DISCOUNTS</text>
        <text x="170" y="140" text-anchor="middle" font-family="Roboto Condensed, sans-serif" font-weight="900" font-style="italic" font-size="24" fill="#1a5fc4">TO YOU</text>
      </g>
    </svg>

    <p class="pitch pitch--lead">WE BOOST YOUR SALES</p>
    <p class="pitch pitch--big">UP TO 100%</p>
    <p class="guarantee"><span class="light">WE </span>GUARANTEE <span class="light">YOU'LL MAKE MORE MONEY</span><br><span class="light">WITH OUR PROGRAM </span>OR YOUR MONEY BACK</p>

    <div class="agent-box">
      <p class="cta">CONTACT AN AGENT NOW</p>
      <p class="phone">1 888 555 0142</p>
    </div>
  </section>

  <div class="photo-strip photo-strip--bottom" role="img" aria-label="Collage of advertiser products: denim, cosmetics, mall catalogue and software">
    <span class="brand-tag" style="left:14px;top:12px">Lanford</span>
    <span class="brand-tag" style="left:200px;top:70px">Avelle</span>
    <span class="brand-tag" style="left:392px;top:12px;color:#1b3f8f">Cloud Plaza</span>
    <span class="brand-tag" style="left:560px;top:12px">Mirawave Store</span>
    <span class="brand-tag" style="left:560px;top:150px">Desk Suite 2012</span>
  </div>

  <footer class="footer">
    <p class="rights">ALL RIGHTS RESERVED &nbsp;|&nbsp; WWW.BRIGHTMERROW.NET</p>
    <p class="sponsor">PROUDLY SPONSORED BY THE PARTICIPATING BUSINESS ENTITIES AND BRIGHT MERROW</p>
  </footer>
</main>
</body>
</html>
```